Maple Bug Guard Business Cards

A modern business card with a predominantly white background and a sleek design featuring Maple with complimentary greys or blacks to convey a professional and contemporary look.

Front:
Primarily white background. Limited use of company purple color can be neighbored by greys.
Text: Name, Title, Cell Phone, Office Phone, Website, email address

Back:
Background Continuation: The back of the card maintains the white background for consistency.
Company name “Maple” in company color and font, “Bug Guard” underneath or underneath left justified of “Maple.”
A subtle pattern or texture in shades of grey to add depth behind the company Logo in font.

logo color: hex #6212ab
font: antique olive nord D Regular

```html
<!DOCTYPE html>
<html lang="en">
<head>
<meta charset="utf-8">
<title>Maple Bug Guard Business Cards</title>
<link rel="stylesheet" href="https://fonts.googleapis.com/css2?family=Archivo:wght@400;700;800&display=swap">
<style>
  :root {
    --brand: #6212ab;
    --brand-soft: #6a3fb0;
    --ink: #3a3a3a;
    --icon: #8a8a8a;
    --paper-back: #eeeef0;
    --texture-light: #f3f3f5;
    --texture-dark: #e2e2e6;
    --paper-front: #ffffff;
    --stage: #e9e6e1;
  }
  * { box-sizing: border-box; margin: 0; padding: 0; }
  html, body {
    width: 840px; height: 1200px; overflow: hidden;
    background: var(--stage);
    font-family: "Archivo", Arial, sans-serif;
  }
  .card {
    position: absolute;
    left: 100px;
    width: 640px;
    height: 410px;
    overflow: hidden;
    box-shadow: 0 1px 3px rgba(0,0,0,0.12);
  }
  .card-back { top: 160px; background: var(--paper-back); }
  .card-front { top: 630px; background: var(--paper-front); }

  .back-texture {
    position: absolute; inset: 0;
    background: radial-gradient(ellipse at center, var(--texture-light) 0%, var(--paper-back) 45%, var(--texture-dark) 100%);
  }

  .company-name {
    position: absolute;
    color: var(--brand);
    font-weight: 800;
    line-height: 1;
    white-space: nowrap;
  }
  .card-back .company-name {
    left: 50%; top: 50%;
    transform: translate(-50%, -50%);
    font-size: 28px;
  }
  .card-front .company-name {
    right: 58px; top: 62px;
    font-size: 26px;
  }

  .name-bar {
    position: absolute; left: 0; top: 100px;
    width: 24px; height: 68px; background: var(--brand-soft);
  }
  .person { position: absolute; left: 50px; top: 106px; }
  .person-name { font-size: 24px; font-weight: 700; color: var(--ink); line-height: 1.2; }
  .person-title { font-size: 17px; font-weight: 400; color: var(--brand-soft); margin-top: 2px; }

  .contact-list { position: absolute; left: 36px; top: 244px; list-style: none; }
  .contact-item {
    display: flex; align-items: center; gap: 14px;
    height: 24px; font-size: 15.5px; font-weight: 700; color: var(--brand-soft);
  }
  .contact-icon { width: 14px; height: 14px; flex: none; }
  .contact-icon * { fill: none; stroke: var(--icon); stroke-width: 1.2; }
</style>
</head>
<body>

<section class="card card-back" aria-label="Card back">
  <div class="back-texture" role="img" aria-label="Subtle grey paper texture behind the company name"></div>
  <p class="company-name">Maple Bug Guard</p>
</section>

<section class="card card-front" aria-label="Card front">
  <p class="company-name">Maple Bug Guard</p>

  <div class="name-bar"></div>
  <div class="person">
    <p class="person-name">Daniel R. Hayes</p>
    <p class="person-title">Manager</p>
  </div>

  <ul class="contact-list">
    <li class="contact-item">
      <svg class="contact-icon" viewBox="0 0 14 14"><rect x="3.5" y="1" width="7" height="12" rx="1"/></svg>
      08xx xxxx xxxx
    </li>
    <li class="contact-item">
      <svg class="contact-icon" viewBox="0 0 14 14"><path d="M1.5 5 Q7 1 12.5 5 L11 6.5 L9 5.5 L5 5.5 L3 6.5 Z"/><rect x="3" y="7.5" width="8" height="5" rx="1"/></svg>
      704-555-0142
    </li>
    <li class="contact-item">
      <svg class="contact-icon" viewBox="0 0 14 14"><circle cx="7" cy="7" r="5.7"/><ellipse cx="7" cy="7" rx="2.5" ry="5.7"/><path d="M1.3 7 H12.7"/></svg>
      maplebugguard.com
    </li>
    <li class="contact-item">
      <svg class="contact-icon" viewBox="0 0 14 14"><rect x="1" y="3" width="12" height="8.5"/><path d="M1 3 L7 8 L13 3"/></svg>
      service@maplebugguard.com
    </li>
    <li class="contact-item">
      <svg class="contact-icon" viewBox="0 0 14 14"><path d="M7 13 C3 8 2.5 6.5 2.5 5.2 A4.5 4.5 0 0 1 11.5 5.2 C11.5 6.5 11 8 7 13 Z"/><circle cx="7" cy="5.3" r="1.6"/></svg>
      Oakridge Vale, NSW, Australia 2999
    </li>
  </ul>
</section>

</body>
</html>
```